QURNB Apothecary
-Designs for stationary is needed: cards, letterhead, envelopes etc...
- The tagline under the mortar and pestle should be placed in one straightline across (instead placed as 2 lines)
- using symbol for email, phone e.g.#75 is good. Note the symbol for email I believe is an envelope.
- use recycle symbol on back (not words) e.g.87
- Background color should be grey (on the back only)
- On the back include faded mortar and pestle with capsules, tagline and recycle symbols e.g. #83
- Don't list website along with phone, fax, email. Place it to the corner in the back and front

```html
<!DOCTYPE html>
<html lang="en">
<head>
<meta charset="utf-8">
<title>QURNB Apothecary – Business Card</title>
<link href="https://fonts.googleapis.com/css2?family=PT+Serif:wght@400;700&family=Arimo:ital,wght@0,400;1,400&display=swap" rel="stylesheet">
<style>
  :root {
    --page-bg: #e9e9e9;
    --card-white: #ffffff;
    --card-grey: #d6d8db;
    --blue-deep: #0a3f9c;
    --blue-mid: #1565c8;
    --blue-light: #5aa8ec;
    --ink: #111111;
    --brand-blue: #2a6fd0;
    --icon-blue: #1554b8;
  }
  * { margin: 0; padding: 0; box-sizing: border-box; }
  html, body { width: 1200px; height: 799px; overflow: hidden; }
  body { background: var(--page-bg); position: relative; }

  .card {
    position: absolute;
    width: 560px;
    height: 340px;
    border-radius: 22px;
    overflow: hidden;
    background: var(--card-white);
    box-shadow: 0 6px 18px rgba(0,0,0,0.18);
  }
  .card-shapes { position: absolute; inset: 0; }
  .card-front { left: 40px; top: 90px; }
  .card-back  { left: 600px; top: 370px; background: var(--card-grey); }

  /* Front */
  .brand {
    position: absolute;
    left: 42px; top: 48px;
    display: flex; align-items: center; gap: 14px;
  }
  .brand-mark {
    width: 46px; height: 46px; border-radius: 50%;
    background: var(--brand-blue);
  }
  .brand-name {
    font-family: "PT Serif", serif;
    font-weight: 700;
    font-size: 34px;
    letter-spacing: 1px;
    color: var(--brand-blue);
    line-height: 1;
  }
  .tagline {
    position: absolute;
    left: 22px; top: 122px;
    font-family: "Arimo", sans-serif;
    font-style: italic;
    font-size: 13px;
    color: var(--blue-deep);
    white-space: nowrap;
  }
  .holder {
    position: absolute;
    left: 150px; top: 168px;
    font-family: "PT Serif", serif;
    color: var(--ink);
    text-align: center;
  }
  .holder-name { font-weight: 700; font-size: 22px; }
  .holder-role { font-weight: 700; font-size: 20px; }
  .website {
    position: absolute;
    right: 26px; bottom: 44px;
    font-family: "PT Serif", serif;
    font-weight: 700;
    font-size: 17px;
    color: var(--card-white);
  }

  /* Back */
  .faded-emblem {
    position: absolute;
    left: 250px; top: 86px;
    width: 150px; height: 150px;
    border-radius: 50%;
    background: radial-gradient(circle, rgba(255,255,255,0.75) 0%, rgba(255,255,255,0) 70%);
  }
  .contact {
    position: absolute;
    left: 30px; top: 46px;
    font-family: "PT Serif", serif;
    font-size: 19px;
    line-height: 1.45;
    color: var(--ink);
  }
  .contact-row { display: flex; align-items: center; gap: 8px; }
  .contact-row.indent { padding-left: 26px; }
  .contact .gap { height: 10px; }
  .icon { width: 18px; height: 18px; flex: none; }
  .recycle-mark {
    position: absolute;
    left: 34px; top: 248px;
    width: 34px; height: 34px;
    border-radius: 50%;
    background: #2f9a4a;
  }
  .back-website {
    position: absolute;
    right: 22px; top: 18px;
    font-family: "PT Serif", serif;
    font-weight: 700;
    font-size: 15px;
    color: var(--card-white);
  }
  .email {
    position: absolute;
    right: 24px; bottom: 16px;
    display: flex; align-items: center; gap: 8px;
    font-family: "PT Serif", serif;
    font-size: 18px;
    color: var(--card-white);
  }
</style>
</head>
<body>

<section class="card card-front" aria-label="Business card front">
  <svg class="card-shapes" viewBox="0 0 560 340" preserveAspectRatio="none">
    <defs>
      <linearGradient id="blueSweep" x1="0" y1="0" x2="1" y2="1">
        <stop offset="0" stop-color="#5aa8ec"/>
        <stop offset="0.5" stop-color="#1565c8"/>
        <stop offset="1" stop-color="#0a3f9c"/>
      </linearGradient>
    </defs>
    <path d="M300 0 L560 0 L560 190 Q540 60 300 0 Z" fill="url(#blueSweep)"/>
    <path d="M0 330 Q260 220 560 200 L560 340 L0 340 Z" fill="url(#blueSweep)"/>
  </svg>

  <div class="brand">
    <span class="brand-mark"></span>
    <span class="brand-name">QURNB Apothecary</span>
  </div>
  <p class="tagline">The Pharmacy that Cares your Health, not just your Prescriptions!</p>

  <div class="holder">
    <p class="holder-name">Lorena Vaskit Pharm.D.</p>
    <p class="holder-role">Director</p>
  </div>

  <p class="website">www.qurnbapothecary.com</p>
</section>

<section class="card card-back" aria-label="Business card back">
  <svg class="card-shapes" viewBox="0 0 560 340" preserveAspectRatio="none">
    <defs>
      <linearGradient id="blueSweepBack" x1="0" y1="0" x2="1" y2="1">
        <stop offset="0" stop-color="#5aa8ec"/>
        <stop offset="0.5" stop-color="#1565c8"/>
        <stop offset="1" stop-color="#0a3f9c"/>
      </linearGradient>
    </defs>
    <path d="M300 0 L560 0 L560 340 L0 340 L0 300 Q420 330 430 170 Q440 40 300 0 Z" fill="url(#blueSweepBack)"/>
  </svg>

  <div class="faded-emblem" role="img" aria-label="Faded mortar and pestle with capsules"></div>

  <div class="contact">
    <p class="contact-row indent">4180 Marlow Ridge Avenue</p>
    <p class="contact-row indent">Suite 120</p>
    <p class="contact-row indent">Brenfield, NC 27390</p>
    <div class="gap"></div>
    <p class="contact-row">
      <svg class="icon" viewBox="0 0 24 24" aria-hidden="true"><path fill="var(--icon-blue)" d="M6.6 10.8a15.1 15.1 0 0 0 6.6 6.6l2.2-2.2a1 1 0 0 1 1-.25 11.4 11.4 0 0 0 3.6.57 1 1 0 0 1 1 1V20a1 1 0 0 1-1 1A17 17 0 0 1 3 4a1 1 0 0 1 1-1h3.5a1 1 0 0 1 1 1c0 1.25.2 2.45.57 3.6a1 1 0 0 1-.25 1z"/></svg>
      <span>Telp:(1111) - 1111 - 1111</span>
    </p>
    <p class="contact-row">
      <svg class="icon" viewBox="0 0 24 24" aria-hidden="true"><path fill="var(--icon-blue)" d="M6 3h9v5H6zM4 9h16a2 2 0 0 1 2 2v6h-4v4H6v-4H2v-6a2 2 0 0 1 2-2zm4 7v3h8v-3z"/></svg>
      <span>Faks:(1111) - 1111 - 1111</span>
    </p>
  </div>

  <div class="recycle-mark" role="img" aria-label="Recycle symbol"></div>

  <p class="back-website">www.qurnbapothecary.com</p>

  <p class="email">
    <svg class="icon" viewBox="0 0 24 24" aria-hidden="true"><path fill="#ffffff" d="M3 5h18a1 1 0 0 1 1 1v12a1 1 0 0 1-1 1H3a1 1 0 0 1-1-1V6a1 1 0 0 1 1-1zm1 2.2V17h16V7.2l-8 5.3z M4.6 7 12 11.9 19.4 7z"/></svg>
    <span>lvaskit@qurnbapothecary.com</span>
  </p>
</section>

</body>
</html>
```